Holiday Rental Company Flyer Design (DL not A5)

Note from PixelFolk Administration: The category sizing selected is A5, however the project requires DL sized artwork. Please refer to the DL template link below while the 'Special Requirements' are updated accordingly.

Project Brief:
We need a double sided DL flyer designed for an up market Holiday Rental Company that portrays a personalised approach to property management. These are to be used for letter box drops to homes we're specifically targeting so the design should be modern, complimentary colour palette, uncluttered & visually appealing.

Please Download the DL Template from Quillmark here: http://www.quillmark.com.au/qm/ns/propath/UploadResources.aspx?selectedTab=0?pfid=BFB&pf_id=BFB&xnav=easypath-upload-image#Templates

Target Market(s)

Wealthy Home Owners

Industry/Entity Type

It Company

Font styles to use
Other font styles liked:
• Avant Garde Extra Light & Demi

Colors
33b8a4

Requirements
Must have
• DL Flyer sizes (210mm width x 99mm width, plus 3mm bleed)
• Front: Logo, Main Image & Grab
• Back: Contact Details & Brief Description of our business
• Images: Ideally the main image should be the house with the pool but alternatively a lifestyle images could also be used.
Nice to have
• A creative designer!
Should not have
• Clutter & busy designs

```html
<!DOCTYPE html>
<html lang="en">
<head>
<meta charset="utf-8">
<title>Bayshore Havens – DL Flyer</title>
<link rel="stylesheet" href="https://fonts.googleapis.com/css2?family=Raleway:wght@200;300&family=Pinyon+Script&family=Libre+Baskerville:ital,wght@0,700;1,400;1,700&display=swap">
<style>
  :root {
    --teal: #19b39a;
    --teal-deep: #12a48c;
    --aqua-panel: #86d9cc;
    --ink: #1b1b1b;
    --black: #000000;
    --white: #ffffff;
    --page: #ffffff;
  }
  * { box-sizing: border-box; margin: 0; padding: 0; }
  html, body { width: 1200px; height: 848px; overflow: hidden; background: var(--page); }

  .flyer { position: relative; width: 1200px; height: 848px; overflow: hidden; }

  /* Front panel */
  .front-photo {
    position: absolute; left: 0; top: 0; width: 563px; height: 848px;
    background:
      radial-gradient(ellipse 200px 160px at 250px 720px, rgba(255,210,140,0.55), transparent 70%),
      radial-gradient(ellipse 180px 300px at 500px 400px, rgba(40,90,230,0.85), transparent 75%),
      linear-gradient(160deg, #6f5fd0 0%, #5a49b8 30%, #2c2a6e 55%, #3b2e2a 75%, #8a6a48 100%);
  }
  .front-wordmark {
    position: absolute; left: 245px; top: 428px;
    transform: translate(-50%, -50%) rotate(-90deg);
    font-family: "Raleway", sans-serif; font-weight: 200;
    color: var(--white); font-size: 66px; line-height: 68px;
    letter-spacing: 9px; text-align: right; white-space: nowrap;
  }

  /* Spine stripe */
  .spine { position: absolute; left: 563px; top: 0; width: 53px; height: 848px; background: var(--teal); }

  /* Back panel */
  .back { position: absolute; left: 616px; top: 0; width: 584px; height: 848px; background: var(--black); }
  .back-photo {
    position: absolute; left: 0; top: 430px; width: 584px; height: 418px;
    background:
      linear-gradient(180deg, #a5896a 0%, #c4a886 20%, #e8d9c4 38%, #d9b94a 60%, #c85a7a 78%, #3e8fa8 100%);
  }
  .back-wordmark {
    position: absolute; left: 0; top: 44px; width: 584px; text-align: center;
    font-family: "Raleway", sans-serif; font-weight: 300;
    color: var(--teal); font-size: 34px; line-height: 38px; letter-spacing: 4px;
  }

  .feature-box {
    position: absolute; left: 48px; top: 242px; width: 479px; height: 456px;
    background: var(--aqua-panel);
    border: 7px dashed var(--teal-deep); border-radius: 12px;
    padding: 18px 20px 0 18px;
    font-family: "Libre Baskerville", serif; color: var(--ink);
  }
  .feature-title {
    font-family: "Pinyon Script", cursive; font-weight: 400;
    font-size: 27px; line-height: 30px; margin-bottom: 12px;
  }
  .feature-copy p {
    font-style: italic; font-size: 11.6px; line-height: 16px;
    text-align: justify; margin-bottom: 14px;
  }
  .benefits { list-style: none; margin: -2px 0 14px; }
  .benefits li {
    font-style: italic; font-size: 11.6px; line-height: 16px;
    margin-bottom: 5px; display: flex; align-items: center; gap: 3px;
  }
  .benefits svg { flex: none; }
  .benefits strong { font-weight: 700; }
  .contact { text-align: center; font-weight: 700; font-size: 12px; line-height: 15px; }
  .contact .phone { font-size: 15px; line-height: 20px; margin-bottom: 2px; }
  .contact .email { font-weight: 400; }
</style>
</head>
<body>
<main class="flyer">
  <section class="front-photo" role="img" aria-label="Photograph of a luxury holiday home at dusk with a lit swimming pool and modern interior"></section>
  <div class="front-wordmark">BAYSHORE<br>HAVENS</div>

  <div class="spine"></div>

  <section class="back">
    <div class="back-photo" role="img" aria-label="Photograph of a bedroom with a colourful geometric quilt and yellow cushions"></div>
    <div class="back-wordmark">BAYSHORE<br>HAVENS</div>

    <div class="feature-box">
      <h2 class="feature-title">What we do differently!</h2>
      <div class="feature-copy">
        <p>Rather than relying upon a key safe or a central pick-up destination, a ‘Bayshore Havens’ staff member will greet guests upon arrival.</p>
        <p>Our ‘Meet &amp; Greet’ service provides home owners with an increased level of Security and also allows us to:</p>
      </div>
      <ul class="benefits">
        <li><svg width="13" height="12" viewBox="0 0 13 12"><path d="M1 6h8M6 2l4 4-4 4" fill="none" stroke="#12a48c" stroke-width="2.2"/></svg><span><strong>Prepare</strong> the home for their arrival (lights, heaters, music etc.)</span></li>
        <li><svg width="13" height="12" viewBox="0 0 13 12"><path d="M1 6h8M6 2l4 4-4 4" fill="none" stroke="#12a48c" stroke-width="2.2"/></svg><span><strong>Establish</strong> a rapport &amp; help facilitate future bookings</span></li>
        <li><svg width="13" height="12" viewBox="0 0 13 12"><path d="M1 6h8M6 2l4 4-4 4" fill="none" stroke="#12a48c" stroke-width="2.2"/></svg><span><strong>Reiterate</strong> their responsibilities to ensure the return of their bond</span></li>
      </ul>
      <div class="feature-copy">
        <p>If you’d like to know what your property could achieve or require additional information, please contact us on:</p>
      </div>
      <address class="contact" style="font-style:normal">
        <div class="phone">(03) 5550 2718</div>
        <div class="email">stay@bayshorehavens.com.au</div>
        <div>www.bayshorehavens.com.au</div>
        <div class="email">PO Box 42, Seacliff. Victoria 3999</div>
      </address>
    </div>
  </section>
</main>
</body>
</html>
```